Pet Sitting Business Card

Would like a business card designed for my new pet sitting business
Card needs to match with logo design.
Blue and Orange are the theme colours.

Simple yet sophisticated design

company name:- MARIGOLD PET CARE
Tessa Brundle
Owner
0462157093
tessa@marigoldpetcare.com.au
www.marigoldpetcare.com.au

I'm going to close my deadline early. I will be picking a winner by the 10th of May. Please submit designs before then.
thank you

Target Market(s)

All types of professional pet lovers wishing to have their pet looked after

Industry/Entity Type

Pet

Requirements
Must have
• Logo design
Blue and orange

```html
<!DOCTYPE html>
<html lang="en">
<head>
<meta charset="utf-8">
<title>Marigold Pet Care – Business Card</title>
<link href="https://fonts.googleapis.com/css2?family=Libre+Baskerville:wght@400;700&display=swap" rel="stylesheet">
<style>
  :root {
    --page: #e9e7e4;
    --sky: #7cc6f0;
    --sky-light: #ffffff;
    --brand-blue: #2a7fd6;
    --orange: #e8802a;
    --orange-soft: #f6b98a;
    --peach: #fde8d6;
    --ink: #2b2b2b;
  }
  * { box-sizing: border-box; margin: 0; padding: 0; }
  html, body { width: 1200px; height: 873px; overflow: hidden; }
  body {
    background: var(--page);
    font-family: "Libre Baskerville", Georgia, serif;
    position: relative;
  }
  .card {
    position: absolute;
    width: 500px;
    height: 286px;
    top: 294px;
    overflow: hidden;
    box-shadow: 0 2px 8px rgba(0,0,0,0.12);
  }
  .card--front {
    left: 70px;
    background: linear-gradient(215deg, var(--sky-light) 0%, #d9eefb 40%, var(--sky) 100%);
  }
  .card--back {
    left: 630px;
    background: linear-gradient(200deg, var(--peach) 0%, var(--orange-soft) 100%);
  }
  .brand {
    display: flex;
    align-items: center;
    gap: 10px;
    color: var(--brand-blue);
    font-weight: 700;
    font-size: 22px;
    letter-spacing: 1px;
    line-height: 1.1;
  }
  .brand__dot {
    width: 18px; height: 18px;
    border-radius: 50%;
    background: var(--orange);
    flex: none;
  }
  .card--front .brand { position: absolute; left: 34px; top: 40px; width: 230px; }
  .person { position: absolute; right: 36px; top: 46px; text-align: right; }
  .person__name {
    color: var(--orange);
    font-weight: 700;
    font-size: 22px;
    text-transform: uppercase;
    letter-spacing: 0.5px;
  }
  .person__role {
    color: var(--ink);
    font-size: 13px;
    letter-spacing: 2px;
    margin-top: 6px;
  }
  .contact { position: absolute; left: 34px; bottom: 30px; color: var(--ink); }
  .contact__row { display: flex; align-items: center; gap: 10px; }
  .contact__phone { font-size: 22px; font-weight: 700; margin-bottom: 10px; }
  .contact__line { font-size: 11px; line-height: 1.6; }
  .contact svg { flex: none; }
  .card--back .brand {
    position: absolute;
    left: 0; right: 0; top: 72px;
    justify-content: center;
    font-size: 24px;
  }
  .back__animals {
    position: absolute;
    left: 0; right: 0; bottom: 18px;
    height: 62px;
    background: linear-gradient(180deg, rgba(232,128,42,0.55), var(--orange));
  }
  .back__band {
    position: absolute;
    left: 0; right: 0; bottom: 0;
    height: 18px;
    background: var(--orange);
  }
</style>
</head>
<body>
  <section class="card card--front">
    <div class="brand"><span class="brand__dot"></span><span>MARIGOLD<br>PET CARE</span></div>
    <div class="person">
      <p class="person__name">Tessa Brundle</p>
      <p class="person__role">OWNER</p>
    </div>
    <div class="contact">
      <div class="contact__row contact__phone">
        <svg width="16" height="18" viewBox="0 0 16 18" aria-hidden="true"><path d="M4 1 L7 5 L5 7 Q7 11 10 13 L12 11 L15 14 L12 17 Q2 13 1 4 Z" fill="#2b2b2b"/></svg>
        <span>0462157093</span>
      </div>
      <div class="contact__row">
        <svg width="16" height="12" viewBox="0 0 16 12" aria-hidden="true"><rect x="0.5" y="0.5" width="15" height="11" fill="none" stroke="#2b2b2b"/><path d="M0.5 0.5 L8 7 L15.5 0.5" fill="none" stroke="#2b2b2b"/></svg>
        <div>
          <p class="contact__line">tessa@marigoldpetcare.com.au</p>
          <p class="contact__line">www.marigoldpetcare.com.au</p>
        </div>
      </div>
    </div>
  </section>

  <section class="card card--back">
    <div class="brand"><span class="brand__dot"></span><span>MARIGOLD PET CARE</span></div>
    <div class="back__animals" role="img" aria-label="Row of orange pet silhouettes: horse, dogs, cats and rabbits"></div>
    <div class="back__band"></div>
  </section>
</body>
</html>
```